Design mobile friendly review and ranking site

We're working on a corporate website for reviewing and ranking fellow employees. We need the website to look both fun and professional and it needs to be responsive - to it works on mobile and desktop.

Looking for css and HTML for 3 key pages as well as a header and footer for the site. Also would need any supporting graphics as part of the design.

Target Market(s)

Professionals in their 20s, 30s, and 40s.

Industry/Entity Type

Internet

Coding

Coded - Design and coding required

Number of Pages Required

3 page

Font styles to use
Sans Serif

Requirements
Must have
• 3 key pages we need (note included screenshots for each - these are just super rough cuts so you see examples of the content.)
• a) main-intro: A compelling into page with a login/registration form. Should be sleek/modern/enticing. Also we would show the ranking for the top 3 people to tease people re: content.
• b) main-page: Has two sections: One at the top where you would rate someone and one at the bottom where it shows a ranking of people.
• c) profile page: This is where you view a specific person. You see the person's picture, some info about the person, you see their overall rating, you can rate them, and you also see their historical ratings.
Nice to have
• Note we need css and HTML for this. It should feel as sleek and modern. Note also must be responsive design so it works well in mobile and desktop.

```html
<!DOCTYPE html>
<html lang="en">
<head>
<meta charset="utf-8">
<title>Peer Standing</title>
<link href="https://fonts.googleapis.com/css2?family=Open+Sans:wght@400;600;700&family=Raleway:wght@300;400;500&display=swap" rel="stylesheet">
<style>
:root{
  --brand:#f2330f;
  --brand-soft:#f15a2b;
  --ink:#222;
  --muted:#555;
  --link:#2a6f96;
  --star-on:#f5a300;
  --star-off:#222;
  --line:#d6d6d6;
  --row-alt:#f4f3f3;
}
*{box-sizing:border-box;margin:0;padding:0}
html,body{width:943px;height:1200px;overflow:hidden;background:#fff}
body{position:relative;font-family:"Open Sans",Arial,sans-serif;color:var(--ink);font-variant-numeric:lining-nums}
.abs{position:absolute}
.site-title{left:58px;top:38px;font-family:"Raleway",sans-serif;font-weight:300;font-size:28px;color:#222;white-space:nowrap}
.share-link{left:63px;top:80px;font-size:12px;color:var(--brand-soft);font-family:"Raleway",sans-serif}
.user-nav{right:59px;top:80px;font-size:12px;font-family:"Raleway",sans-serif;font-variant-numeric:lining-nums;display:flex;gap:6px;align-items:center;white-space:nowrap}
.user-nav .ico{display:inline-block;width:9px;height:9px;background:var(--brand-soft);border-radius:2px;margin-right:4px;vertical-align:-1px}
.header-rule{left:0;top:107px;width:943px;height:1px;background:#777}
.hero-photo{left:46px;top:131px;width:849px;height:209px;background:linear-gradient(90deg,#ef5a3c,#e8472a 50%,#f0674a)}
.profile-photo{left:57px;top:280px;width:120px;height:120px;border-radius:50%;border:3px solid #fff;background:radial-gradient(circle at 50% 40%,#8a8a8a,#2e2e2e)}
.hero-name{left:195px;top:300px;font-family:"Raleway",sans-serif;font-size:24px;font-weight:500;color:#fff}
.rate-prompt{left:210px;top:375px;font-size:13px;font-family:"Raleway",sans-serif;font-weight:500}
.rating-bar{display:flex;border:1px solid var(--line);height:30px;width:613px;background:#fff;font-size:12.5px;color:var(--muted);white-space:nowrap}
.rating-bar .cell{display:flex;align-items:center;justify-content:center;gap:7px;border-right:1px solid var(--line)}
.rating-bar .cell:last-child{border-right:0}
.rating-bar .c1{width:196px}.rating-bar .c2{width:207px}.rating-bar .c3{width:210px}
.stars{letter-spacing:1px;font-size:12px}
.stars .on{color:var(--star-on)}.stars .off{color:var(--star-off)}
.comment-label{left:209px;top:466px;width:260px;font-size:12.5px;color:var(--muted);line-height:17px}
.comment-box{left:483px;top:470px;width:340px;height:93px;border:1px solid #ccc}
.btn{background:var(--brand);color:#fff;border:0;font-family:"Open Sans",sans-serif;display:flex;align-items:center;justify-content:center;border-radius:2px}
.btn-reviews{left:209px;top:515px;width:104px;height:26px;font-size:11.5px;gap:5px}
.btn-action{top:580px;width:65px;height:28px;font-size:13px;font-weight:700;letter-spacing:.5px}
.btn-skip{left:687px}.btn-save{left:758px}
.filter-band{left:47px;top:636px;width:848px;height:64px;background:linear-gradient(90deg,#e8452a,#f2330f 30%,#ef3a16)}
.select{top:656px;height:25px;background:#fff;font-size:13px;display:flex;align-items:center;padding-left:8px;border-radius:2px}
.select::after{content:"";position:absolute;right:9px;top:10px;border:4px solid transparent;border-top:5px solid #333}
.filter-word{top:660px;color:#fff;font-size:13px}
.rank-row{left:47px;width:848px;height:133px}
.rank-row.alt{background:var(--row-alt);border:1px solid var(--line)}
.avatar{width:64px;height:64px;border-radius:50%;background:var(--brand)}
.rank-label{width:140px;text-align:center;font-size:12.5px}
.rank-name{width:160px;text-align:center;font-size:16px;white-space:nowrap}
.stats{font-size:12.5px;display:flex;gap:7px;white-space:nowrap}
.stats .num{color:var(--brand-soft);margin-right:14px}
.stats .details{color:var(--link)}
.site-footer{left:0;top:1161px;width:943px;height:39px;background:var(--brand)}
.copyright{left:48px;top:1173px;color:#fff;font-size:11.5px;font-family:"Raleway",sans-serif}
.social{top:1170px;width:23px;height:23px;border-radius:50%;background:#fff;border:1px solid #ddd}
</style>
</head>
<body>
<header>
  <h1 class="abs site-title">Peer Standing</h1>
  <a class="abs share-link">Share this to get more points!</a>
  <nav class="abs user-nav"><span>Level 3 - 41points to Level4</span><span>|</span><span><i class="ico"></i>Your Profile</span><span>|</span><span><i class="ico"></i>Log Out</span></nav>
  <div class="abs header-rule"></div>
</header>

<section class="rate-panel">
  <div class="abs hero-photo" role="img" aria-label="Office workspace photo with red tint"></div>
  <div class="abs profile-photo" role="img" aria-label="Portrait photo of Michael"></div>
  <h2 class="abs hero-name">Michael</h2>
  <p class="abs rate-prompt">Anonymously rate this person for a point</p>
  <div class="abs rating-bar" style="left:210px;top:414px">
    <div class="cell c1">Smart <span class="stars"><span class="on">★★★★</span><span class="off">★</span></span></div>
    <div class="cell c2">Average Personality <span class="stars"><span class="on">★★★</span><span class="off">★★</span></span></div>
    <div class="cell c3">Works Crazy Hard <span class="stars"><span class="on">★★★★★</span></span></div>
  </div>
  <p class="abs comment-label">(Optional) Write an anonymous comment about this person</p>
  <div class="abs comment-box"></div>
  <a class="abs btn btn-reviews"><svg width="11" height="8" viewBox="0 0 11 8"><ellipse cx="5.5" cy="4" rx="5" ry="3.5" fill="#fff"/><circle cx="5.5" cy="4" r="1.6" fill="#f2330f"/></svg>View Reviews</a>
  <a class="abs btn btn-action btn-skip">SKIP</a>
  <a class="abs btn btn-action btn-save">SAVE</a>
</section>

<section class="ranking">
  <div class="abs filter-band" role="img" aria-label="Office photo strip with red tint"></div>
  <div class="abs select" style="left:208px;width:104px">Best</div>
  <span class="abs filter-word" style="left:325px">in</span>
  <div class="abs select" style="left:348px;width:169px">All Functions</div>
  <span class="abs filter-word" style="left:530px">and</span>
  <div class="abs select" style="left:566px;width:169px">All Levels</div>

  <div class="abs rank-row alt" style="top:720px"></div>
  <div class="abs avatar" style="left:86px;top:732px" role="img" aria-label="Profile placeholder"></div>
  <div class="abs rank-label" style="left:47px;top:800px">#1 Best</div>
  <div class="abs rank-name" style="left:37px;top:816px">Jim Johns</div>
  <div class="abs stats" style="left:211px;top:749px">Points <span class="num">4.1</span> Number of reviews <span class="num">5</span><span class="details">View Details</span></div>
  <div class="abs rating-bar" style="left:210px;top:771px">
    <div class="cell c1">Smart <span class="stars"><span class="on">★★★</span><span class="off">★★</span></span></div>
    <div class="cell c2">Average Personality <span class="stars"><span class="on">★★★</span><span class="off">★★</span></span></div>
    <div class="cell c3">Works Crazy Hard <span class="stars"><span class="on">★★★</span><span class="off">★★</span></span></div>
  </div>

  <div class="abs avatar" style="left:87px;top:867px" role="img" aria-label="Profile placeholder"></div>
  <div class="abs rank-label" style="left:47px;top:936px">#2 Best</div>
  <div class="abs rank-name" style="left:39px;top:953px">Michael</div>
  <div class="abs stats" style="left:211px;top:882px">Points <span class="num">4</span> Number of reviews <span class="num">5</span><span class="details">View Details</span></div>
  <div class="abs rating-bar" style="left:210px;top:905px">
    <div class="cell c1">Smart <span class="stars"><span class="on">★★★</span><span class="off">★★</span></span></div>
    <div class="cell c2">Average Personality <span class="stars"><span class="on">★★★</span><span class="off">★★</span></span></div>
    <div class="cell c3">Works Crazy Hard <span class="stars"><span class="on">★★★</span><span class="off">★★</span></span></div>
  </div>

  <div class="abs rank-row alt" style="top:986px"></div>
  <div class="abs avatar" style="left:86px;top:999px" role="img" aria-label="Profile placeholder"></div>
  <div class="abs rank-label" style="left:47px;top:1067px">#3 Best</div>
  <div class="abs rank-name" style="left:37px;top:1084px">Joel Navarro III</div>
  <div class="abs stats" style="left:211px;top:1015px">Points <span class="num">3.6</span> Number of reviews <span class="num">5</span><span class="details">View Details</span></div>
  <div class="abs rating-bar" style="left:210px;top:1038px">
    <div class="cell c1">Smart <span class="stars"><span class="on">★★</span><span class="off">★★★</span></span></div>
    <div class="cell c2">Average Personality <span class="stars"><span class="on">★★★</span><span class="off">★★</span></span></div>
    <div class="cell c3">Works Crazy Hard <span class="stars"><span class="on">★★★</span><span class="off">★★</span></span></div>
  </div>
</section>

<footer>
  <div class="abs site-footer"></div>
  <p class="abs copyright">© Copyright information here</p>
  <span class="abs social" style="left:764px"></span>
  <span class="abs social" style="left:791px"></span>
  <span class="abs social" style="left:818px"></span>
  <span class="abs social" style="left:845px"></span>
</footer>
</body>
</html>
```